Web design for Vantor Ledgerly

We need to redesign and update the website for www.vantorledgerly.io, if you'll look, you can see it is very poorly done.

The content won't change much (the founders page will go away though). I've attached a logo and flyer we are using that may provide inspiration for the design, though you don't have to make it consistent with the flyer.

Industry/Entity Type

Hr technology

Coding

Coded - Design and coding required

Number of Pages Required

5+ page

Requirements
Must have
• To be hosted with NestHarbor

```html
<!DOCTYPE html>
<html lang="en">
<head>
<meta charset="utf-8">
<title>Vantor Ledgerly</title>
<link rel="stylesheet" href="https://fonts.googleapis.com/css2?family=Poppins:wght@400;500;600;700&display=swap">
<style>
:root{
  --blue:#4f93f3;
  --blue-dark:#2e5183;
  --navy:#2c4c7c;
  --ink:#1c1f2a;
  --text:#3a3d46;
  --muted:#6d7280;
  --hero-bg:#f0f5fd;
  --soft-bg:#f5f8fe;
  --card:#ffffff;
  --line:#e4e9f2;
  --photo:#d6e8fc;
}
*{box-sizing:border-box;margin:0;padding:0}
html,body{width:1200px;height:4570px;overflow:hidden}
body{font-family:"Poppins",sans-serif;color:var(--text);background:#fff;position:relative}
a{text-decoration:none;color:inherit}

/* top bar */
.topbar{position:absolute;top:0;left:0;width:1200px;height:40px;background:#fff;font-size:11px;color:var(--muted)}
.topbar .item{position:absolute;top:13px;display:flex;align-items:center;gap:10px}
.social{position:absolute;right:118px;top:15px;display:flex;gap:24px}
.social span{width:9px;height:9px;border-radius:50%;background:var(--blue-dark);display:block}

/* nav */
.nav{position:absolute;top:40px;left:0;width:1200px;height:79px;background:var(--blue)}
.brand{position:absolute;left:108px;top:24px;display:flex;align-items:center;gap:10px;color:#fff;font-weight:600;font-size:15px}
.brand i{width:28px;height:28px;border:2px solid #fff;border-radius:50%;display:block}
.menu{position:absolute;left:399px;top:30px;display:flex;gap:34px;color:#fff;font-size:14px}
.nav-btn{position:absolute;left:927px;top:22px;width:160px;height:36px;background:#fff;color:var(--blue);font-size:12px;display:flex;align-items:center;justify-content:center}

/* hero */
.hero{position:absolute;top:119px;left:0;width:1200px;height:603px;background:var(--hero-bg)}
.eyebrow{font-size:14px;color:var(--text)}
.hero .eyebrow{position:absolute;left:108px;top:112px}
.hero h1{position:absolute;left:108px;top:144px;font-size:45px;font-weight:600;color:var(--ink);letter-spacing:1px}
.hero p{position:absolute;left:108px;top:240px;width:490px;font-size:20px;line-height:35.5px;color:var(--ink)}
.btn{position:absolute;background:var(--blue);color:#fff;font-size:15px;display:flex;align-items:center;justify-content:center;gap:8px}
.hero .btn{left:108px;top:431px;width:236px;height:59px}
.hero-art{position:absolute;left:595px;top:121px;width:270px;height:355px;background:linear-gradient(160deg,#e3eaf8,#d3dbef);border-radius:6px}
.hero-art.wide{left:595px;width:270px}
.hero-art-b{position:absolute;left:685px;top:215px;width:370px;height:265px;background:linear-gradient(160deg,#e3eaf8,#d3dbef);border-radius:6px}

/* featured */
.featured{position:absolute;top:722px;left:0;width:1200px;height:201px;background:#fff}
.featured .eyebrow{position:absolute;left:108px;top:66px}
.partners{position:absolute;left:108px;top:124px;width:984px;display:flex;justify-content:space-between;align-items:center;font-size:24px;color:#555a63}
.partners span{display:flex;align-items:center;gap:8px}
.partners i{width:26px;height:26px;border-radius:50%;background:#555a63;display:block}

/* about */
.about{position:absolute;top:923px;left:0;width:1200px;height:612px;background:#fff}
.about .eyebrow{position:absolute;left:108px;top:76px}
.about h2{position:absolute;left:108px;top:114px;width:430px;font-size:27px;line-height:37px;font-weight:600;color:var(--ink);letter-spacing:-1px}
.about p{position:absolute;left:108px;top:276px;width:500px;font-size:17px;line-height:35px;color:var(--ink)}
.btn-outline{position:absolute;left:108px;top:501px;width:167px;height:60px;border:1.5px solid var(--blue);color:var(--blue);font-size:15px;display:flex;align-items:center;justify-content:center;gap:8px}
.about-bg{position:absolute;left:610px;top:90px;width:590px;height:522px;background:radial-gradient(circle at 70% 40%,#eef3fc,#fff 70%)}
.about-photo{position:absolute;left:680px;top:99px;width:392px;height:418px;background:linear-gradient(180deg,var(--photo),#c9dcf3)}

/* services */
.services{position:absolute;top:1535px;left:0;width:1200px;height:1261px;background:var(--soft-bg)}
.center{position:absolute;left:0;width:1200px;text-align:center}
.services .lbl{top:123px;font-size:14px}
.services h2{top:152px;font-size:28px;font-weight:600;color:var(--ink);letter-spacing:-1px}
.services .sub{top:213px;font-size:17px;line-height:35px;color:var(--ink)}
.card{position:absolute;width:307px;background:var(--card);text-align:center}
.card .ico{width:78px;height:78px;border-radius:50%;background:#eef3fb;margin:46px auto 0;display:flex;align-items:center;justify-content:center}
.card h3{font-size:18px;font-weight:500;color:var(--ink);line-height:25px;margin:26px 20px 0}
.card p{font-size:14px;line-height:25px;color:var(--text);margin:12px 34px 0}
.card .more{position:absolute;left:0;width:100%;font-size:14px;color:var(--blue)}

/* stats */
.stats{position:absolute;top:2796px;left:108px;width:984px;height:257px;background:#fff;border-left:1px solid var(--line);border-right:1px solid var(--line)}
.stat{position:absolute;top:0;width:240px;text-align:center}
.stat svg{margin-top:52px}
.stat b{display:block;font-size:28px;font-weight:600;color:var(--blue-dark);margin-top:12px}
.stat b em{font-style:normal;color:var(--blue)}
.stat span{font-size:16px;color:var(--text)}

/* cta */
.cta{position:absolute;top:3053px;left:0;width:1200px;height:563px;background:var(--navy)}
.cta h2{position:absolute;left:108px;top:147px;font-size:34px;font-weight:600;color:#fff;letter-spacing:-1.5px}
.cta p{position:absolute;left:108px;top:222px;width:390px;font-size:20px;line-height:35px;color:#fff}
.cta .btn{left:108px;top:401px;width:243px;height:57px}
.cta-art{position:absolute;left:550px;top:142px;width:542px;height:337px;background:linear-gradient(150deg,#5a7fb4,#3b5f94);border-radius:6px}

/* contact */
.contact{position:absolute;top:3616px;left:0;width:1200px;height:893px;background:#fff}
.contact-box{position:absolute;left:108px;top:120px;width:984px;height:737px;background:var(--navy)}
.contact-box .lbl{position:absolute;left:58px;top:191px;font-size:14px;color:#fff}
.contact-box h2{position:absolute;left:58px;top:224px;font-size:32px;font-weight:600;color:#fff;letter-spacing:-1.5px}
.info{position:absolute;left:58px;display:flex;gap:24px}
.info i{width:26px;height:26px;border-radius:50%;background:#4a6ea3;display:flex;align-items:center;justify-content:center;margin-top:6px}
.info small{display:block;font-size:12px;letter-spacing:4px;color:#c9d6ea}
.info strong{display:block;font-size:15px;font-weight:500;color:#fff;margin-top:6px;letter-spacing:.5px}
.form{position:absolute;left:469px;top:84px;width:456px;height:582px;background:var(--hero-bg)}
.form h3{position:absolute;left:31px;top:66px;font-size:17px;font-weight:500;color:var(--ink)}
.field{position:absolute;left:31px;width:394px;height:54px;background:#fff;border:1px solid var(--line);font-size:13px;color:var(--muted);padding:18px 22px}
.form .send{position:absolute;left:31px;top:484px;width:394px;height:46px;background:var(--blue);color:#fff;font-size:15px;display:flex;align-items:center;justify-content:center}

/* footer */
.footer{position:absolute;top:4509px;left:100px;width:1000px;height:61px;border-top:1px solid var(--line);font-size:11px;color:var(--text)}
.footer .copy{position:absolute;left:12px;top:24px}
.footer .links{position:absolute;right:8px;top:24px;display:flex;gap:28px}
.to-top{position:absolute;left:1145px;top:4455px;width:30px;height:30px;border:1.5px solid var(--blue);border-radius:50%;display:flex;align-items:center;justify-content:center}
</style>
</head>
<body>

<header class="topbar">
  <div class="item" style="left:125px">
    <svg width="10" height="12" viewBox="0 0 10 12"><path d="M5 0a4 4 0 0 1 4 4c0 3-4 8-4 8S1 7 1 4a4 4 0 0 1 4-4z" fill="#2e5183"/><circle cx="5" cy="4" r="1.5" fill="#fff"/></svg>
    Northfield, Ridgeport, Bayview
  </div>
  <div class="item" style="left:363px">
    <svg width="12" height="12" viewBox="0 0 12 12"><path d="M2 1l2 0 1 3-1.5 1a7 7 0 0 0 3.5 3.5L8 7l3 1v2a1 1 0 0 1-1 1A9 9 0 0 1 1 2a1 1 0 0 1 1-1z" fill="#2e5183"/></svg>
    +1 555-014-2290
  </div>
  <div class="social" aria-label="Social links"><span></span><span></span><span></span></div>
</header>

<nav class="nav">
  <div class="brand"><i></i>Vantor Ledgerly</div>
  <div class="menu"><a>Home</a><a>About</a><a>Services</a><a>Testimonial</a><a>Blog</a><a>Contact</a></div>
  <a class="nav-btn">Contact Now</a>
</nav>

<section class="hero">
  <div class="eyebrow">All your data in one place</div>
  <h1>VANTOR LEDGERLY</h1>
  <p>We provide a Managed Cloud Data Platform PaaS that becomes the “brains” of your enterprise HR technology, connecting and centralizing all HR data availability.</p>
  <a class="btn">Schedule A Meeting
    <svg width="16" height="10" viewBox="0 0 16 10"><path d="M0 5h14M10 1l4 4-4 4" stroke="#fff" stroke-width="1.5" fill="none"/></svg></a>
  <div class="hero-art-b" role="img" aria-label="Illustration of a desktop monitor with floating data documents" style="left:595px;top:121px;width:265px;height:120px"></div>
  <div class="hero-art-b" role="img" aria-label="Illustration of a desktop monitor showing data panels"></div>
</section>

<section class="featured">
  <div class="eyebrow">Featured In</div>
  <div class="partners">
    <span><i></i>zavori</span>
    <span><i></i>HALDENRIX</span>
    <span><i></i>quellna</span>
    <span>fernoquay</span>
    <span>velmisto<i></i></span>
  </div>
</section>

<section class="about">
  <div class="about-bg"></div>
  <div class="eyebrow">About me</div>
  <h2>I am Darren Holloway, a Chief Data Officer, Skyvault Data Advisory, Inc., a data warehousing consultancy.</h2>
  <p>I am an expert at reducing time to insight and aligning technology with business with over 20 years data engineering and data analytics experience for companies such as Meridian Trust, Corbel Toolworks, Atlas Remit, Brightwave Media.</p>
  <a class="btn-outline">Know More
    <svg width="16" height="10" viewBox="0 0 16 10"><path d="M0 5h14M10 1l4 4-4 4" stroke="#4f93f3" stroke-width="1.5" fill="none"/></svg></a>
  <div class="about-photo" role="img" aria-label="Portrait photo of the founder holding a coffee cup"></div>
</section>

<section class="services">
  <div class="center lbl">Services</div>
  <h2 class="center">What we provide</h2>
  <div class="center sub">What we consider when we create your repository of<br>HR historical data</div>

  <div class="card" style="left:112px;top:341px;height:391px">
    <div class="ico"><svg width="34" height="34" viewBox="0 0 34 34" fill="none" stroke="#2e5183" stroke-width="1.5"><rect x="5" y="8" width="24" height="18"/><path d="M3 30h28M10 14h14M10 20h14"/></svg></div>
    <h3>Streamline Application<br>Implementation</h3>
    <p>Makes system implementations and upgrades easier with better data quality.</p>
    <a class="more" style="top:335px">Tell Me More →</a>
  </div>
  <div class="card" style="left:447px;top:341px;height:391px">
    <div class="ico"><svg width="34" height="34" viewBox="0 0 34 34" fill="none" stroke="#2e5183" stroke-width="1.5"><rect x="8" y="4" width="18" height="26" rx="2"/><path d="M12 11h10M12 17h10M12 23h6"/></svg></div>
    <h3>Manage Data<br>Effectively</h3>
    <p>Effective data management requires expert skills and experience.</p>
    <a class="more" style="top:335px">Tell Me More →</a>
  </div>
  <div class="card" style="left:781px;top:341px;height:391px">
    <div class="ico"><svg width="34" height="34" viewBox="0 0 34 34" fill="none" stroke="#2e5183" stroke-width="1.5"><rect x="5" y="6" width="7" height="22"/><rect x="14" y="6" width="7" height="22"/><rect x="23" y="6" width="7" height="22"/></svg></div>
    <h3>Future<br>Proof</h3>
    <p>New innovations<br>keep you ahead of<br>your competitors.</p>
    <a class="more" style="top:335px">Tell Me More →</a>
  </div>

  <div class="card" style="left:112px;top:765px;height:368px">
    <div class="ico"><svg width="34" height="34" viewBox="0 0 34 34" fill="none" stroke="#2e5183" stroke-width="1.5"><rect x="4" y="4" width="12" height="9"/><rect x="18" y="21" width="12" height="9"/><path d="M10 13v8h8M24 21V13"/></svg></div>
    <h3>Model Your Organization</h3>
    <p>Model the way your organization really is, not the way your vendor sees it.</p>
    <a class="more" style="top:317px">Tell Me More →</a>
  </div>
  <div class="card" style="left:447px;top:765px;height:368px">
    <div class="ico"><svg width="34" height="34" viewBox="0 0 34 34" fill="none" stroke="#2e5183" stroke-width="1.5"><circle cx="8" cy="9" r="3"/><circle cx="8" cy="17" r="3"/><circle cx="8" cy="25" r="3"/><path d="M14 9h16M14 17h16M14 25h16"/></svg></div>
    <h3>Gain Insights into your<br>Workforce</h3>
    <p>Provides the platform for strategic analytics and machine learning.</p>
    <a class="more" style="top:317px">Tell Me More →</a>
  </div>
  <div class="card" style="left:781px;top:765px;height:368px">
    <div class="ico"><svg width="34" height="34" viewBox="0 0 34 34" fill="none" stroke="#2e5183" stroke-width="1.5"><path d="M17 4v24M8 30h18M6 10h22M6 10l-4 9h8zM28 10l-4 9h8z"/></svg></div>
    <h3>Leverage Cloud-Native<br>Capabilities</h3>
    <p>Focus on the needs of your business, not the technology.</p>
    <a class="more" style="top:317px">Tell Me More →</a>
  </div>
</section>

<section class="stats">
  <div class="stat" style="left:0">
    <svg width="40" height="42" viewBox="0 0 40 42" fill="none" stroke="#2e5183" stroke-width="1.5"><circle cx="20" cy="13" r="8"/><path d="M5 40c0-9 7-15 15-15s15 6 15 15z"/></svg>
    <b>2500<em>+</em></b><span>Happy Clients</span>
  </div>
  <div class="stat" style="left:240px">
    <svg width="40" height="42" viewBox="0 0 40 42" fill="none" stroke="#2e5183" stroke-width="1.5"><rect x="8" y="5" width="24" height="34" rx="2"/><rect x="15" y="2" width="10" height="6"/><circle cx="20" cy="20" r="4"/><path d="M13 32c1-5 13-5 14 0"/></svg>
    <b>500<em>+</em></b><span>Case Completed</span>
  </div>
  <div class="stat" style="left:480px">
    <svg width="46" height="42" viewBox="0 0 46 42" fill="none" stroke="#2e5183" stroke-width="1.5"><rect x="3" y="4" width="40" height="28"/><path d="M11 13h24M15 19h16"/><circle cx="23" cy="32" r="4"/><path d="M20 35l-2 6M26 35l2 6"/></svg>
    <b>10<em>+</em></b><span>Years of Experience</span>
  </div>
  <div class="stat" style="left:720px">
    <svg width="42" height="42" viewBox="0 0 42 42" fill="none" stroke="#2e5183" stroke-width="1.5"><circle cx="21" cy="21" r="18"/><path d="M13 21l6 6 10-12"/></svg>
    <b>100<em>%</em></b><span>Happy Clients</span>
  </div>
</section>

<section class="cta">
  <h2>Ready to find out more?</h2>
  <p>Are you ready to optimize your implementation and use of HR technology? Contact us for more information.</p>
  <a class="btn">Request Assessment
    <svg width="16" height="10" viewBox="0 0 16 10"><path d="M0 5h14M10 1l4 4-4 4" stroke="#fff" stroke-width="1.5" fill="none"/></svg></a>
  <div class="cta-art" role="img" aria-label="Illustration of a person beside a large checkmark circle with plants"></div>
</section>

<section class="contact">
  <div class="contact-box">
    <div class="lbl">Contact me</div>
    <h2>Let’s Talk</h2>
    <div class="info" style="top:323px">
      <i><svg width="10" height="12" viewBox="0 0 10 12"><path d="M5 0a4 4 0 0 1 4 4c0 3-4 8-4 8S1 7 1 4a4 4 0 0 1 4-4z" fill="#fff"/></svg></i>
      <div><small>Location</small><strong>Northfield, Ridgeport, Bayview</strong></div>
    </div>
    <div class="info" style="top:421px">
      <i><svg width="12" height="12" viewBox="0 0 12 12"><path d="M2 1l2 0 1 3-1.5 1a7 7 0 0 0 3.5 3.5L8 7l3 1v2a1 1 0 0 1-1 1A9 9 0 0 1 1 2a1 1 0 0 1 1-1z" fill="#fff"/></svg></i>
      <div><small>Contact</small><strong>+1 555-014-2290</strong></div>
    </div>
    <div class="info" style="top:519px">
      <i><svg width="12" height="10" viewBox="0 0 12 10"><rect x="0.5" y="0.5" width="11" height="9" fill="#fff"/><path d="M1 1l5 4 5-4" stroke="#4a6ea3" fill="none"/></svg></i>
      <div><small>Email</small><strong>info@vantorledgerly.io</strong></div>
    </div>

    <form class="form">
      <h3>Get in touch</h3>
      <div class="field" style="top:110px">Full Name</div>
      <div class="field" style="top:183px">Email Address</div>
      <div class="field" style="top:257px">Subject</div>
      <div class="field" style="top:330px;height:130px">Your Message</div>
      <div class="send">Send Request</div>
    </form>
  </div>
</section>

<a class="to-top" aria-label="Back to top"><svg width="10" height="12" viewBox="0 0 10 12"><path d="M5 12V1M1 5l4-4 4 4" stroke="#4f93f3" stroke-width="1.5" fill="none"/></svg></a>

<footer class="footer">
  <div class="copy">Copyright © 2022 Vantor Ledgerly. All Rights Reserved.</div>
  <div class="links"><a>Privacy Policies</a><a>Terms and Conditions</a></div>
</footer>

</body>
</html>
```